New Website Announcement

We need a flyer to announce our new website to customers and prospective clients. The website will be launching soon, but I can provide a detailed outline in PDF form with copy and imagery to serve as inspiration for this design.

I would like a postcard size document that can be mailed in an envelope (no need for postcard style mailer info on 1 side)

About my company:

Clearwater Lantern Group is a new breed of marketing consulting agency built for the next frontier of consumer learning. Social interaction will be at the heart of great insights going forward – in how consumers engage with brands and in how organizations socialize what they learn to gain competitive advantage.
By fusing innovative insights techniques, technology and compelling graphic design-based reporting, we ensure results get noticed and make an impact.

contact info that can also be included:

Email: morgan@clearwater-lantern.com

Phone: 518-732-6148

New High Res logo file has been added. (.ai)

Thanks

Reason: Giving more time next week for submissions. This project has been committed. Thanks !

Attention all designers submitting a design for this project. Please keep in mind a few important details about this project.

1. Remember that the main objective of this postcard is to announce my new website.

2. Please be sure to read the brief for the copy I would like on each side. You can be creative in how it is displayed, but I need this key information somewhere. All other copy on the attached files is for your background only.

3. Please do not submit overly simple designs that just take the images I provided and overlay a text box with my copy. I could easily do this myself in PowerPoint in 5 minutes.

4. Remember that the design should be edgy and modern but needs to be professional and speak to a business audience.

Please submit any questions. Thank you for your submissions. 

Morgan

Illustrator high res logo file now correctly uploaded. Thanks.

Target Market(s)

senior level marketing and research clients at large companies and agencies

Industry/Entity Type

Marketing

Requirements
Must have
• Main message:

Need an engaging way to tell customers and prospective clients that we have a new website and that they should come visit us online to learn more about out services, check out case studies and read about our exciting partnerships.

COPY TO USE - UPDATED

Side 1:
(logo)
Introducing Clearwater Lantern Group

Let’s talk about taking research out of the dark ages.

Visit our newly launched website to learn how and get in touch.

www.clearwater-lantern.com

Side 2
Logo
followed by tagline:
Consumer insights that get noticed.
A leading-edge marketing partnership that really works.

Additional text to use on Side 2:
How we can help...

Think of us as your go-to resource for identifying and incorporating the most innovative and exciting techniques into your research programs. We carefully curate and develop close partnerships with the best of the best - from online qualitative research and mobile ethnography to social media listening and fresh takes on concept testing, we can guide the way.

Plus, we believe that socializing consumer learning is just as critical as gathering it.By taking insights deliverables to the next level – through infographics, videos, magazines,interactive profiles and so much more – we are getting stakeholders excited to engage with research and inspired to take action because of it.
It’s a new way to look at insights from a new type of partner. And, it’s a new way to get the most from your research dollars.
Nice to have
• could incorporate our website main image of the lamp on white brick background which is attached, but not 100% mandatory.
Should not have
• - should not be too playful or young, but needs to be modern and design focused

- should not be cluttered or overly 'salesy'

- needs to be upscale and elegant / compelling and aligned with the look and feel of the website imagery (see attached)

```html
<!DOCTYPE html>
<html lang="en">
<head>
<meta charset="utf-8">
<title>Clearwater Lantern Group — New Website</title>
<link rel="stylesheet" href="https://fonts.googleapis.com/css2?family=Titillium+Web:wght@600;700&family=Great+Vibes&family=Graduate&family=Nunito+Sans:wght@300&display=swap">
<style>
  :root {
    --ink: #1b1b1b;
    --strip: #000000;
    --brand-blue: #1279c4;
    --white: #ffffff;
    --ring: #d9d9d9;
    --url-tint: #e4e4e4;
    --wall-light: #f4f4f2;
    --wall-mid: #d8d8d6;
    --floor-light: #cfcfcd;
    --floor-dark: #a9a9a7;
  }
  html, body {
    margin: 0;
    padding: 0;
    overflow: hidden;
  }
  .flyer {
    position: relative;
    width: 1200px;
    height: 932px;
    overflow: hidden;
    font-family: "Titillium Web", Arial, sans-serif;
    color: var(--ink);
  }
  .scene-backdrop {
    position: absolute;
    inset: 0;
    background:
      radial-gradient(ellipse 420px 260px at 500px 250px, rgba(255,255,255,0.9), rgba(255,255,255,0) 70%),
      linear-gradient(to bottom, var(--wall-light) 0, var(--wall-mid) 640px, #bdbdbb 672px, var(--floor-light) 676px, var(--floor-dark) 932px);
  }
  .headline {
    position: absolute;
    left: 0;
    width: 1078px;
    top: 352px;
    margin: 0;
    text-align: center;
    font-size: 23px;
    font-weight: 700;
    line-height: 1;
  }
  .scatter-word {
    position: absolute;
    font-weight: 600;
    line-height: 1;
  }
  .closing {
    position: absolute;
    left: 0;
    width: 1086px;
    top: 497px;
    margin: 0;
    text-align: center;
    font-size: 31px;
    font-weight: 600;
    line-height: 1;
  }
  .url-band {
    position: absolute;
    left: 0;
    top: 768px;
    width: 1200px;
    height: 94px;
    background: var(--brand-blue);
  }
  .url-text {
    position: absolute;
    left: 40px;
    top: 786px;
    margin: 0;
    font-family: "Graduate", "Rockwell", serif;
    font-size: 43px;
    line-height: 58px;
    letter-spacing: 0.5px;
    color: var(--url-tint);
  }
  .brand-strip {
    position: absolute;
    left: 962px;
    top: 0;
    width: 104px;
    height: 932px;
    background: var(--strip);
  }
  .intro-word {
    position: absolute;
    left: 990px;
    top: 40px;
    writing-mode: vertical-rl;
    font-family: "Great Vibes", cursive;
    font-size: 36px;
    line-height: 1;
    color: var(--white);
  }
  .brand-seal {
    position: absolute;
    left: 882px;
    top: 235px;
    width: 266px;
    height: 266px;
    box-sizing: border-box;
    border-radius: 50%;
    background: var(--strip);
    border: 5px solid var(--ring);
    display: flex;
    align-items: center;
    justify-content: center;
  }
  .brand-name {
    margin: 0;
    text-align: center;
    font-family: "Titillium Web", Arial, sans-serif;
    font-weight: 700;
    font-size: 34px;
    line-height: 1.05;
    letter-spacing: 1px;
    text-transform: uppercase;
    color: var(--white);
  }
  .contact-list {
    position: absolute;
    left: 992px;
    top: 538px;
    writing-mode: vertical-rl;
    font-family: "Nunito Sans", Arial, sans-serif;
    font-weight: 300;
    font-size: 24px;
    line-height: 40px;
    color: var(--white);
    margin: 0;
    padding: 0;
    list-style: none;
  }
  .contact-item {
    display: flex;
    align-items: center;
    gap: 8px;
  }
  .contact-icon {
    width: 20px;
    height: 20px;
    flex: none;
  }
</style>
</head>
<body>
  <main class="flyer">
    <div class="scene-backdrop" role="img" aria-label="Photo of a black arched floor lamp glowing against a whitewashed brick wall above a concrete floor"></div>

    <p class="headline">Let’s talk about taking research out of the dark ages.</p>

    <span class="scatter-word" style="left:254px;top:424px;font-size:23px">Visit</span>
    <span class="scatter-word" style="left:318px;top:434px;font-size:19px">our</span>
    <span class="scatter-word" style="left:371px;top:420px;font-size:19px">newly</span>
    <span class="scatter-word" style="left:448px;top:436px;font-size:27px">launched</span>
    <span class="scatter-word" style="left:562px;top:447px;font-size:21px">website</span>
    <span class="scatter-word" style="left:647px;top:425px;font-size:19px">to</span>
    <span class="scatter-word" style="left:675px;top:439px;font-size:27px">learn</span>
    <span class="scatter-word" style="left:749px;top:425px;font-size:21px">how</span>

    <p class="closing">and get in touch!</p>

    <div class="url-band"></div>
    <p class="url-text">WWW.CLEARWATER-LANTERN.COM</p>

    <div class="brand-strip"></div>
    <div class="intro-word">Introducing</div>

    <div class="brand-seal">
      <p class="brand-name">Clearwater<br>Lantern<br>Group</p>
    </div>

    <ul class="contact-list">
      <li class="contact-item">
        <svg class="contact-icon" viewBox="0 0 20 20" aria-hidden="true">
          <rect x="2" y="4" width="16" height="12" fill="none" stroke="#fff" stroke-width="1.6"/>
          <path d="M2 4 L10 11 L18 4" fill="none" stroke="#fff" stroke-width="1.6"/>
        </svg>
        <span>morgan@clearwater-lantern.com</span>
      </li>
      <li class="contact-item">
        <svg class="contact-icon" viewBox="0 0 20 20" aria-hidden="true">
          <path d="M5 2 L8 2 L9 6 L7 8 C8 11 9 12 12 13 L14 11 L18 12 L18 15 C18 17 16 18 14 18 C8 17 3 12 2 6 C2 4 3 2 5 2 Z" fill="#fff"/>
        </svg>
        <span>518-732-6148</span>
      </li>
    </ul>
  </main>
</body>
</html>
```